Do i have coronavirus, flue or cold?

Using information from QRV and government agencies we want to make a easy to read infographic helping patients see if they have coronavirus, the flu or a cold. Using a flow diagram or whatever you think will make it easy to read and digest for the average lamen.

Information is in the word document and in the chart.

We are www.tovipharm.co.uk attached is our brand guidelines, we will be putting this infographic on our website and email/sms it to all of our 300,000 patients.

```html
<!DOCTYPE html>
<html lang="en">
<head>
<meta charset="utf-8">
<title>Do I have coronavirus, flu or cold?</title>
<link href="https://fonts.googleapis.com/css2?family=Poppins:ital,wght@0,400;0,600;0,700;0,800;1,400&display=swap" rel="stylesheet">
<style>
  :root {
    --stage: #454545;
    --frame: #7689c6;
    --card: #ffffff;
    --ink: #3d47a0;
    --ink-body: #2e3590;
    --navy: #23256a;
    --badge: #3e4aa0;
    --row-tint: #fdf3ef;
    --rule: #c9d6ea;
    --icon-tone: #e9ebf6;
  }
  * { box-sizing: border-box; margin: 0; padding: 0; }
  html, body { width: 1200px; height: 1200px; overflow: hidden; background: var(--stage); }
  body { font-family: "Poppins", sans-serif; position: relative; }

  .poster {
    position: absolute; left: 157px; top: 0;
    width: 1160px; height: 1570px;
    background: var(--frame);
    transform: scale(0.7643); transform-origin: 0 0;
  }
  .card {
    position: absolute; left: 54px; top: 54px; width: 1046px; height: 1362px;
    background: var(--card); border-radius: 6px;
  }
  .badge {
    position: absolute; left: 811px; top: 0; width: 188px; height: 102px;
    background: var(--badge); color: #fff; border-radius: 0 0 8px 8px;
    font-weight: 700; font-size: 20px; line-height: 1.25; padding: 24px 0 0 29px;
  }
  .badge .big { font-size: 24px; }
  .title {
    position: absolute; left: 48px; top: 60px; width: 755px;
    font-size: 37px; font-weight: 600; color: var(--ink); letter-spacing: 1.8px;
    white-space: nowrap; line-height: 1.2;
  }

  .chart { position: absolute; left: 29px; top: 136px; width: 992px; }
  .bar { display: grid; grid-template-columns: 307px 685px; height: 8px; }
  .bar span:first-child { background: var(--navy); }
  .bar span:last-child { background: var(--frame); }

  .head, .row { display: grid; grid-template-columns: 307px 228px 228px 229px; }
  .head { height: 159px; }
  .head > div { padding: 14px 0 0 22px; }
  .head > div + div { border-left: 1px solid var(--rule); }
  .col-title { font-size: 34px; font-weight: 600; color: var(--ink); letter-spacing: 1.5px; line-height: 1.3; }
  .col-note { font-size: 21px; color: var(--ink-body); line-height: 1.22; margin-top: 22px; }

  .row { height: 100px; border-bottom: 1px solid var(--rule); }
  .row.tall { height: 113px; }
  .row:last-child { border-bottom: 0; height: 99px; }
  .row:nth-child(even) { background: var(--row-tint); }
  .row > div { padding: 20px 0 0 22px; font-size: 21px; color: var(--ink-body); line-height: 1.15; }
  .row > div + div { border-left: 1px solid var(--rule); }
  .row .symptom {
    position: relative; font-weight: 800; color: var(--ink); line-height: 1.38;
    border-bottom: 1px solid var(--navy); margin-bottom: -1px;
  }
  .symptom-icon {
    position: absolute; right: 28px; top: 12px; width: 84px; height: 76px;
    border-radius: 10px; background: var(--icon-tone);
  }

  .source {
    position: absolute; right: 77px; top: 1330px;
    font-size: 15px; font-style: italic; color: var(--ink);
  }

  .footer-brand {
    position: absolute; left: 193px; top: 1470px;
    display: flex; align-items: center; gap: 10px;
    color: #fff; font-weight: 600; font-size: 28px;
  }
  .footer-brand .mark { width: 22px; height: 22px; background: #fff; }
  .footer-info {
    position: absolute; left: 419px; top: 1462px;
    color: #fff; font-size: 19px; line-height: 1.25;
  }
  .footer-info strong { font-weight: 700; font-size: 20px; }
  .footer-link { position: absolute; left: 743px; top: 1470px; width: 203px; text-align: center; color: #fff; }
  .footer-link .visit { font-size: 12px; }
  .footer-link .url {
    margin-top: 2px; height: 23px; border-radius: 12px; background: #fff;
    color: var(--badge); font-weight: 700; font-size: 15px; line-height: 23px;
  }
</style>
</head>
<body>
  <div class="poster">
    <div class="card">
      <div class="badge">Coronavirus<br><span class="big">(COVID-19)</span></div>
      <h1 class="title">Do I have coronavirus, flu or cold?</h1>

      <div class="chart">
        <div class="bar"><span></span><span></span></div>
        <div class="head">
          <div><div class="col-title">Symptoms</div></div>
          <div><div class="col-title">COVID-19</div><div class="col-note">Symptoms<br>range from mild<br>to severe</div></div>
          <div><div class="col-title">Flu</div><div class="col-note">Abrupt onset<br>of symptoms</div></div>
          <div><div class="col-title">Cold</div><div class="col-note">Gradual onset<br>of symptoms</div></div>
        </div>
        <div class="bar"><span></span><span></span></div>

        <div class="rows">
          <div class="row"><div class="symptom">Fever<span class="symptom-icon" role="img" aria-label="Thermometer icon"></span></div><div>Common</div><div>Common</div><div>Rare</div></div>
          <div class="row"><div class="symptom">Cough<span class="symptom-icon" role="img" aria-label="Head outline coughing icon"></span></div><div>Common</div><div>Common</div><div>Common</div></div>
          <div class="row"><div class="symptom">Sore Throat<span class="symptom-icon" role="img" aria-label="Head outline with sore throat icon"></span></div><div>Sometimes</div><div>Common</div><div>Common</div></div>
          <div class="row"><div class="symptom">Shortness<br>of Breath<span class="symptom-icon" role="img" aria-label="Head outline breathing out icon"></span></div><div>Sometimes</div><div>No</div><div>No</div></div>
          <div class="row"><div class="symptom">Fatigue<span class="symptom-icon" role="img" aria-label="Person resting in bed icon"></span></div><div>Sometimes</div><div>Common</div><div>Sometimes</div></div>
          <div class="row"><div class="symptom">Aches<br>&amp; Pains<span class="symptom-icon" role="img" aria-label="Figure with shoulder pain icon"></span></div><div>Sometimes</div><div>Common</div><div>No</div></div>
          <div class="row"><div class="symptom">Headaches<span class="symptom-icon" role="img" aria-label="Head outline with headache icon"></span></div><div>Sometimes</div><div>Common</div><div>Common</div></div>
          <div class="row"><div class="symptom">Runny or<br>Stuffy Nose<span class="symptom-icon" role="img" aria-label="Head outline with runny nose icon"></span></div><div>Sometimes</div><div>Sometimes</div><div>Common</div></div>
          <div class="row tall"><div class="symptom">Diarrhea<span class="symptom-icon" role="img" aria-label="Figure seated on toilet icon"></span></div><div>Rare</div><div>Sometimes,<br>especially for<br>children</div><div>No</div></div>
          <div class="row"><div class="symptom">Sneezing<span class="symptom-icon" role="img" aria-label="Head outline sneezing icon"></span></div><div>No</div><div>No</div><div>Common</div></div>
        </div>
      </div>

      <p class="source">Adapted from material produced by QRV, National Disease Agency.</p>
    </div>

    <div class="footer-brand"><span class="mark"></span>Tovi Pharm</div>
    <div class="footer-info">For more information about<br><strong>Coronavirus (COVID-19)</strong></div>
    <div class="footer-link"><div class="visit">visit</div><div class="url">www.qrv.int</div></div>
  </div>
</body>
</html>
```